Prepare a modern, professional business card for Meridel Vantage Advisory (MVA) Our company is in the banking, compliance and finance industry. We provide kiosks, software integration, and compliance guidelines so that banks can "bank" Marijuana Dispensaries with MonLex, Office of Statute Review and NBRA approval.

Target Market(s)

Banks

Industry/Entity Type

Business

Contact Information for Business Card

Peter L Oakridge
Meridel Vantage Advisory
Vice President
4427 Larkspur Crossing Way
Suite 218
Halvern City, NV 89990
pete@mvalq.com
555-418-7362

Font styles to use
Sans Serif

Requirements
Nice to have
• I like the clean simple appearance of Quince computers. Perhaps the three LETTERS of MVA can be the LOGO on the Card and the Company name could be incorporated in the contact information. Like colors of white, black and gray

```html
<!DOCTYPE html>
<html lang="en">
<head>
<meta charset="utf-8">
<title>Meridel Vantage Advisory – Business Card</title>
<link rel="stylesheet" href="https://fonts.googleapis.com/css2?family=Josefin+Sans:wght@300;700&family=Open+Sans:wght@400&display=swap">
<style>
  :root {
    --page-bg: #ffffff;
    --card-bg: #333333;
    --text-light: #e4e4e4;
    --text-muted: #d6d6d6;
    --mark-grey: #9a9a9a;
    --icon-grey: #7a7a7a;
  }
  * { margin: 0; padding: 0; box-sizing: border-box; }
  html, body {
    width: 1200px; height: 1200px; overflow: hidden;
    background: var(--page-bg);
  }
  .card {
    position: absolute; left: 240px; top: 411px;
    width: 795px; height: 466px;
    background: var(--card-bg);
    font-family: "Josefin Sans", sans-serif;
  }
  .company-name {
    position: absolute; left: 110px; top: 66px;
    font-weight: 300; font-size: 33px; letter-spacing: 1.5px;
    color: var(--text-muted); white-space: nowrap;
  }
  .person {
    position: absolute; left: 103px; top: 122px;
    display: flex; align-items: baseline; white-space: nowrap;
    font-weight: 300; color: var(--text-light);
  }
  .person-name { font-size: 39px; letter-spacing: 0.3px; }
  .divider {
    display: inline-block; width: 4px; height: 34px;
    background: var(--text-light); margin: 0 16px 0 16px;
    align-self: center; transform: translateY(-4px);
  }
  .person-title { font-size: 28px; }
  .brand-mark {
    position: absolute; left: 138px; top: 296px;
    font-weight: 700; font-size: 100px; line-height: 1;
    color: var(--mark-grey); letter-spacing: -4px;
  }
  .contact-list {
    position: absolute; left: 448px; top: 271px;
    list-style: none;
    font-family: "Open Sans", sans-serif; font-size: 14px;
    color: var(--text-light);
  }
  .contact-item {
    display: flex; align-items: flex-start; gap: 18px;
    line-height: 21px; margin-bottom: 17px;
  }
  .contact-icon { flex: 0 0 18px; width: 18px; height: 18px; margin-top: 1px; }
</style>
</head>
<body>
  <section class="card" aria-label="Business card">
    <h1 class="company-name">MERIDEL VANTAGE ADVISORY</h1>
    <p class="person">
      <span class="person-name">PETER L OAKRIDGE</span>
      <span class="divider" aria-hidden="true"></span>
      <span class="person-title">Vice President</span>
    </p>

    <div class="brand-mark">MVA</div>

    <ul class="contact-list">
      <li class="contact-item">
        <svg class="contact-icon" viewBox="0 0 18 18" aria-hidden="true">
          <circle cx="9" cy="9" r="8" fill="var(--icon-grey)"/>
          <rect x="5" y="6" width="8" height="6" fill="none" stroke="#fff" stroke-width="1"/>
          <path d="M5 6 L9 9.5 L13 6" fill="none" stroke="#fff" stroke-width="1"/>
        </svg>
        <span>pete@mvalq.com</span>
      </li>
      <li class="contact-item">
        <svg class="contact-icon" viewBox="0 0 18 18" aria-hidden="true">
          <circle cx="9" cy="9" r="8" fill="var(--icon-grey)"/>
          <path d="M7 5 Q5 6 6 9 Q8 12.5 11 13 Q12.5 13 13 12 L11.5 10.5 L10.5 11.2 Q8.5 10 7.8 8 L8.6 7 Z" fill="#fff"/>
        </svg>
        <span>555-418-7362</span>
      </li>
      <li class="contact-item">
        <svg class="contact-icon" viewBox="0 0 18 18" aria-hidden="true">
          <circle cx="9" cy="9" r="8" fill="var(--icon-grey)"/>
          <path d="M9 4.5 L13.5 8.8 H12 V13 H10 V10.5 H8 V13 H6 V8.8 H4.5 Z" fill="#fff"/>
        </svg>
        <span>4427 Larkspur Crossing Way Suite,<br>218 Halvern City, NV 89990</span>
      </li>
    </ul>
  </section>
</body>
</html>
```